Life and business Coaching Business Card and Logo

A new design for new company. We coach people to get the best out of themselves in business, life, health , family, career, relationships.
we work in Professional, executive, business and corporate environment. We use art and the processes of making art to work with getting people to delve into and change their mind maps or the way they are currently thinking so that they can move forward towards their goals strategically.
Updates

Project Deadline Extended
Reason: I have been laid up in bed with back problems and have just been able to get back to view designs. several are quiet good and I have given feedback today. I also want to take my project off refundable status as I will choose a design from this brief. regards Marisol

Target Market(s)

Professional artistic and bold energetic individuals

Industry/Entity Type

Health

Contact Information for Business Card

Vel5Mentoring, Marisol Drayke, Shaping Days Boldly,
Mob:0419586740, Ph: +61 8 95820647,
Professional, Executive, Business and Corporate Coach

Requirements
Must have
• a logo that can be used on all promotional and stationary material.
Should contain a person and be bold/colourful, simple and artistic.
Nice to have
• Room to place qualifications of Business

```html
<!DOCTYPE html>
<html lang="en">
<head>
<meta charset="utf-8">
<title>Vel5Mentoring Business Card</title>
<link rel="stylesheet" href="https://fonts.googleapis.com/css2?family=Open+Sans:wght@400;600;700&family=Kalam:wght@400&display=swap">
<style>
  :root {
    --backdrop: #9a9a9a;
    --card: #ffffff;
    --green-dark: #567a2b;
    --green-text: #4f7a2a;
    --green-name: #7aa832;
    --green-rule: #a6c574;
    --green-deep: #3d5220;
    --green-glow: #b9d04a;
  }
  html, body {
    margin: 0;
    padding: 0;
    width: 1200px;
    height: 960px;
    overflow: hidden;
    background: var(--backdrop);
    font-family: "Open Sans", Arial, sans-serif;
  }
  .canvas { position: relative; width: 1200px; height: 960px; }
  .card {
    position: absolute;
    width: 716px;
    height: 428px;
    background: var(--card);
    overflow: hidden;
  }
  .card--front { left: 262px; top: 44px; }
  .card--back { left: 260px; top: 502px; }

  .brand {
    position: absolute;
    display: flex;
    align-items: center;
    gap: 8px;
    color: var(--green-dark);
    font-weight: 600;
    white-space: nowrap;
  }
  .brand__dot { border-radius: 50%; background: var(--green-name); flex: none; }
  .card--front .brand { left: 44px; top: 74px; font-size: 20px; }
  .card--front .brand__dot { width: 14px; height: 14px; }

  .services-list {
    position: absolute;
    left: 244px;
    top: 46px;
    margin: 0;
    padding: 0;
    list-style: none;
    color: var(--green-text);
    font-size: 18px;
    line-height: 27px;
  }
  .holder-name {
    position: absolute;
    left: 36px;
    top: 166px;
    margin: 0;
    color: var(--green-name);
    font-size: 26px;
    font-weight: 400;
    line-height: 34px;
  }
  .name-rule {
    position: absolute;
    left: 18px;
    top: 200px;
    width: 680px;
    height: 1px;
    background: var(--green-rule);
  }
  .tagline {
    position: absolute;
    left: 36px;
    top: 202px;
    margin: 0;
    color: var(--green-dark);
    font-family: "Kalam", cursive;
    font-size: 18px;
    letter-spacing: 0.5px;
  }
  .contact {
    position: absolute;
    right: 40px;
    top: 240px;
    margin: 0;
    text-align: right;
    color: var(--green-text);
    font-size: 18px;
    font-weight: 600;
    line-height: 26px;
  }
  .footer-band {
    position: absolute;
    left: 0;
    right: 0;
    top: 316px;
    bottom: 0;
    background: linear-gradient(90deg, var(--green-dark) 0%, var(--green-glow) 55%, var(--green-dark) 100%);
  }

  .card--back .brand {
    left: 0; right: 0; top: 140px;
    justify-content: center;
    font-size: 46px;
    gap: 14px;
  }
  .card--back .brand__dot { width: 30px; height: 30px; }
  .roles {
    position: absolute;
    left: 0; right: 0; top: 383px;
    display: flex;
    justify-content: center;
    align-items: center;
    color: var(--green-deep);
    font-size: 18px;
    font-weight: 600;
  }
  .roles__divider {
    width: 1px; height: 22px;
    background: var(--green-deep);
    margin: 0 16px;
  }
</style>
</head>
<body>
<div class="canvas">
  <section class="card card--front">
    <div class="footer-band" role="img" aria-label="Decorative green wave band along the bottom of the card"></div>
    <div class="brand"><span class="brand__dot"></span>Vel5Mentoring</div>
    <ul class="services-list">
      <li>Professional</li>
      <li>Executive</li>
      <li>Business and Corporate Coach</li>
    </ul>
    <h1 class="holder-name">Marisol Drayke</h1>
    <div class="name-rule"></div>
    <p class="tagline">Shaping Days Boldly</p>
    <p class="contact">[Mobile]&nbsp; 0419586740<br>[Phone] +61 8 95820647</p>
  </section>

  <section class="card card--back">
    <div class="brand"><span class="brand__dot"></span>Vel5Mentoring</div>
    <div class="roles">
      <span>Professional</span>
      <span class="roles__divider"></span>
      <span>Executive</span>
      <span class="roles__divider"></span>
      <span>Business and Corporate Coach</span>
    </div>
  </section>
</div>
</body>
</html>
```